Stationery Design for Consulting Company
Orvel Partners
Creative Brief
Professional
Tomas Wenholt
Director
Orvel Partners LLC 48215 Ridgefern Road Dunmore, DE 19872 USA
tomas@orvel-advisory.com
www.orvel-advisory.com
Maybe just a larger logo in the middle unless you have better ideas. I'm open to suggestions.

```html
<!DOCTYPE html>
<html lang="en">
<head>
<meta charset="utf-8">
<title>Orvel Partners – Business Card</title>
<link href="https://fonts.googleapis.com/css2?family=Montserrat:wght@400;500;600;700&display=swap" rel="stylesheet">
<style>
  :root {
    --backdrop: #c9c9c9;
    --card: #ffffff;
    --brand: #f5a623;
    --ink: #3a3a3a;
    --ink-soft: #6b6b6b;
    --bar-dark: #2e2e2e;
  }
  * { margin: 0; padding: 0; box-sizing: border-box; }
  html, body { width: 1200px; height: 895px; overflow: hidden; }
  body {
    background: var(--backdrop);
    font-family: "Montserrat", sans-serif;
    color: var(--ink);
    display: flex;
    align-items: center;
    justify-content: center;
    gap: 60px;
  }
  .card {
    width: 525px;
    height: 300px;
    background: var(--card);
    position: relative;
    overflow: hidden;
    box-shadow: 0 6px 18px rgba(0,0,0,.18);
  }
  .brand { display: flex; flex-direction: column; }
  .brand-name {
    display: flex; align-items: center; gap: 10px;
    color: var(--brand);
    font-weight: 700;
    letter-spacing: .5px;
  }
  .brand-square { width: 16px; height: 16px; background: var(--brand); }
  .brand-tagline {
    font-size: 8px; letter-spacing: 2px; text-transform: uppercase;
    color: var(--ink-soft); margin-top: 4px;
  }

  /* Back of card */
  .card-back { display: flex; align-items: center; justify-content: center; }
  .card-back .brand { align-items: center; }
  .card-back .brand-name { font-size: 34px; }
  .card-back .brand-square { width: 22px; height: 22px; }
  .card-back .brand-tagline { font-size: 9px; margin-top: 8px; }

  /* Front of card */
  .card-front { padding: 30px 34px; }
  .card-front .brand-name { font-size: 24px; }
  .person { margin-top: 22px; }
  .person-name { font-size: 15px; font-weight: 600; letter-spacing: 1.5px; text-transform: uppercase; }
  .person-title { font-size: 9px; letter-spacing: 2px; text-transform: uppercase; color: var(--ink-soft); margin-top: 3px; }
  .contact {
    position: absolute; left: 34px; right: 34px; top: 170px;
    display: flex; justify-content: space-between;
    font-size: 10px; color: var(--ink);
  }
  .contact-list { list-style: none; display: flex; flex-direction: column; gap: 8px; }
  .contact-list li { display: flex; align-items: center; gap: 8px; }
  .contact-list svg { width: 11px; height: 11px; flex: none; fill: var(--ink-soft); }
  .footer-bar { position: absolute; left: 0; right: 0; bottom: 22px; height: 9px; display: flex; }
  .footer-bar .accent { width: 52%; background: var(--brand); }
  .footer-bar .dark { flex: 1; background: var(--bar-dark); }
</style>
</head>
<body>

<section class="card card-front">
  <div class="brand">
    <div class="brand-name"><span class="brand-square"></span>Orvel Partners LLC</div>
    <div class="brand-tagline">Strategy · Operations · Advisory</div>
  </div>
  <div class="person">
    <div class="person-name">Tomas Wenholt</div>
    <div class="person-title">General Manager</div>
  </div>
  <div class="contact">
    <ul class="contact-list">
      <li>
        <svg viewBox="0 0 24 24"><path d="M12 2a7 7 0 0 0-7 7c0 5 7 13 7 13s7-8 7-13a7 7 0 0 0-7-7zm0 9.5A2.5 2.5 0 1 1 12 6.5a2.5 2.5 0 0 1 0 5z"/></svg>
        <span>48215 Ridgefern Road<br>Dunmore, DE 19872</span>
      </li>
      <li>
        <svg viewBox="0 0 24 24"><circle cx="12" cy="12" r="10"/></svg>
        <span>www.orvel-advisory.com</span>
      </li>
    </ul>
    <ul class="contact-list">
      <li>
        <svg viewBox="0 0 24 24"><path d="M6.6 10.8a15 15 0 0 0 6.6 6.6l2.2-2.2a1 1 0 0 1 1-.25 11.4 11.4 0 0 0 3.6.57 1 1 0 0 1 1 1V20a1 1 0 0 1-1 1A17 17 0 0 1 3 4a1 1 0 0 1 1-1h3.5a1 1 0 0 1 1 1c0 1.25.2 2.45.57 3.57a1 1 0 0 1-.25 1z"/></svg>
        <span>302 555 0148</span>
      </li>
      <li>
        <svg viewBox="0 0 24 24"><rect x="6" y="2" width="12" height="20" rx="2"/></svg>
        <span>302 555 0176</span>
      </li>
      <li>
        <svg viewBox="0 0 24 24"><path d="M2 5h20v14H2z M2 5l10 8 10-8" /></svg>
        <span>tomas@orvel-advisory.com</span>
      </li>
    </ul>
  </div>
  <div class="footer-bar"><span class="accent"></span><span class="dark"></span></div>
</section>

<section class="card card-back">
  <div class="brand">
    <div class="brand-name"><span class="brand-square"></span>Orvel Partners LLC</div>
    <div class="brand-tagline">Strategy · Operations · Advisory</div>
  </div>
</section>

</body>
</html>
```